'Quarrystone Co' Business Cards

Quarrystone Co is a clothing company geared toward people in the mining industry who are crushing it (literally) We need a design for a business card that has 'QS' similar to the layout of the inspo photo below. Rock textures and maybe some rock dust (see GIF). I Included SVG of our circle logo but not sure how to include without it being boring, would like some ideas. Front should say 'Quarrystone Co.' (and 'clothing' in smaller letters below) Back should have our webpage 'quarrystoneco.ca' our email 'info@quarrystoneco.ca' plus a FB and IG icon

```html
<!DOCTYPE html>
<html lang="en">
<head>
<meta charset="utf-8">
<title>Quarrystone Co. Business Cards</title>
<link href="https://fonts.googleapis.com/css2?family=Roboto:wght@300;400;700;900&display=swap" rel="stylesheet">
<style>
  :root {
    --backdrop: #a5a4a5;
    --card-dark: #2b2b2b;
    --rock-deep: #1a1a19;
    --rock-dark: #252523;
    --rock-mid: #34332f;
    --rock-light: #45433e;
    --rock-pale: #55534d;
    --ink-white: #f4f4f4;
    --ink-soft: #c9c9c9;
    --mark-fill: #5a5a5a;
    --back-name: #464646;
    --rule: #6a6a6a;
  }
  * { margin: 0; padding: 0; box-sizing: border-box; }
  html, body {
    width: 1200px;
    height: 927px;
    overflow: hidden;
    background: var(--backdrop);
    font-family: "Roboto", Arial, sans-serif;
  }
  .sheet {
    width: 1200px;
    height: 927px;
    display: flex;
    flex-direction: column;
    align-items: center;
    justify-content: center;
    gap: 60px;
  }
  .card {
    position: relative;
    width: 620px;
    height: 354px;
    border-radius: 3px;
    overflow: hidden;
    box-shadow: 0 10px 24px rgba(0,0,0,0.25);
  }

  /* Front */
  .card-front .rock-texture {
    position: absolute;
    inset: 0;
    background:
      radial-gradient(ellipse 120px 60px at 12% 18%, rgba(85,83,77,0.55) 0%, transparent 100%),
      radial-gradient(ellipse 90px 140px at 88% 30%, rgba(26,26,25,0.7) 0%, transparent 100%),
      radial-gradient(ellipse 160px 70px at 70% 82%, rgba(69,67,62,0.6) 0%, transparent 100%),
      radial-gradient(ellipse 70px 50px at 40% 8%, rgba(26,26,25,0.6) 0%, transparent 100%),
      radial-gradient(ellipse 110px 80px at 22% 88%, rgba(26,26,25,0.55) 0%, transparent 100%),
      radial-gradient(ellipse 200px 90px at 55% 45%, rgba(85,83,77,0.35) 0%, transparent 100%),
      radial-gradient(ellipse 60px 40px at 95% 92%, rgba(85,83,77,0.5) 0%, transparent 100%),
      radial-gradient(ellipse 80px 30px at 62% 18%, rgba(69,67,62,0.5) 0%, transparent 100%),
      linear-gradient(155deg, var(--rock-light) 0%, var(--rock-mid) 35%, var(--rock-dark) 70%, var(--rock-deep) 100%);
  }
  .front-mark {
    position: absolute;
    left: 46px;
    top: 50%;
    transform: translateY(-50%);
    width: 262px;
    height: 262px;
    border-radius: 50%;
    background: radial-gradient(circle at 40% 35%, rgba(255,255,255,0.05), rgba(0,0,0,0.18));
    border: 2px solid rgba(0,0,0,0.5);
    box-shadow: inset 0 2px 6px rgba(0,0,0,0.45), 0 1px 0 rgba(255,255,255,0.08);
  }
  .front-name {
    position: absolute;
    right: 40px;
    top: 50%;
    transform: translateY(-50%);
    text-align: center;
    color: var(--ink-white);
  }
  .brand-name {
    font-weight: 900;
    font-size: 26px;
    letter-spacing: 0.5px;
    text-transform: uppercase;
    line-height: 1;
  }
  .brand-tagline {
    margin-top: 8px;
    font-weight: 300;
    font-size: 11px;
    letter-spacing: 7px;
    text-transform: uppercase;
    color: var(--ink-soft);
  }

  /* Back */
  .card-back { background: var(--card-dark); }
  .back-brand {
    position: absolute;
    left: 0; right: 0;
    top: 92px;
    display: flex;
    align-items: center;
    justify-content: center;
    gap: 14px;
  }
  .back-brand .dot {
    width: 60px;
    height: 60px;
    border-radius: 50%;
    background: var(--mark-fill);
  }
  .back-brand .brand-name {
    font-size: 56px;
    color: var(--back-name);
    letter-spacing: 1px;
  }
  .contact-line {
    position: absolute;
    left: 0; right: 0;
    top: 212px;
    text-align: center;
    font-weight: 300;
    font-size: 15px;
    color: var(--ink-soft);
  }
  .social-row {
    position: absolute;
    left: 0; right: 0;
    top: 246px;
    display: flex;
    align-items: center;
    justify-content: center;
    gap: 10px;
  }
  .social-row .rule {
    width: 150px;
    height: 1px;
    background: linear-gradient(90deg, transparent, var(--rule));
  }
  .social-row .rule.right {
    background: linear-gradient(90deg, var(--rule), transparent);
  }
  .social-row .social-dot {
    width: 18px;
    height: 18px;
    border-radius: 50%;
    background: var(--ink-soft);
  }
</style>
</head>
<body>
  <main class="sheet">
    <section class="card card-front">
      <div class="rock-texture" role="img" aria-label="Dark slate rock texture with faint dust"></div>
      <div class="front-mark"></div>
      <div class="front-name">
        <div class="brand-name">Quarrystone Co.</div>
        <div class="brand-tagline">Clothing</div>
      </div>
    </section>

    <section class="card card-back">
      <div class="back-brand">
        <span class="dot"></span>
        <span class="brand-name">Quarrystone</span>
      </div>
      <p class="contact-line">info@quarrystoneco.ca | www.quarrystoneco.ca</p>
      <div class="social-row">
        <span class="rule"></span>
        <span class="social-dot"></span>
        <span class="social-dot"></span>
        <span class="rule right"></span>
      </div>
    </section>
  </main>
</body>
</html>
```